Korvale Power Solutions Business Card

We are based in Columbus, Ohio and need a business card that represents our modern approach to energy projects. We perform energy projects for buildings that include Heating/Cooling Controls, Mechanical Equipment, LED Lighting, Envelope Improvements, etc. We have saved clients up to 65% of their total energy costs. Our logo is attached. We like designs that integrate our logo into one side and then provide contact/person info on the other. We would like to limit the number of colors to keep printing costs down. We want to maintain the blue/green in our logo.

```html
<!DOCTYPE html>
<html lang="en">
<head>
<meta charset="UTF-8">
<title>Korvale Power Solutions Business Card</title>
<link href="https://fonts.googleapis.com/css2?family=Open+Sans:wght@400;600;700&family=Montserrat:wght@700&display=swap" rel="stylesheet">
<style>
  :root {
    --blue: #3d84c6;
    --blue-dark: #2a6aa8;
    --green: #74b94a;
    --white: #ffffff;
    --ink: #4a4f55;
    --rule: #d6dade;
    --backdrop: #8c7a62;
  }
  * { margin: 0; padding: 0; box-sizing: border-box; }
  html, body { width: 711px; height: 1200px; overflow: hidden; }
  body {
    background: var(--backdrop);
    font-family: "Open Sans", Arial, sans-serif;
    position: relative;
  }
  .side-label {
    position: absolute;
    left: 24px;
    font-family: "Montserrat", Arial, sans-serif;
    font-weight: 700;
    font-size: 46px;
    color: var(--white);
    letter-spacing: 1px;
  }
  .side-label.front { top: 10px; }
  .side-label.back { top: 610px; }

  .card {
    position: absolute;
    left: 75px;
    width: 560px;
    height: 320px;
    background: var(--white);
    border-radius: 4px;
    overflow: hidden;
    box-shadow: 0 10px 24px rgba(0,0,0,0.35);
  }
  .card.front-card { top: 170px; }
  .card.back-card { top: 770px; }

  /* front */
  .name-band {
    height: 86px;
    background: var(--blue);
    color: var(--white);
    padding: 18px 34px 0 0;
    text-align: right;
  }
  .person-name {
    font-size: 24px;
    font-weight: 700;
    letter-spacing: 2px;
    text-transform: uppercase;
  }
  .person-title {
    font-size: 13px;
    letter-spacing: 1px;
    opacity: 0.9;
  }
  .front-body {
    display: flex;
    align-items: center;
    height: 206px;
    padding: 0 30px;
  }
  .brand-mark {
    display: flex;
    align-items: center;
    gap: 10px;
    width: 230px;
  }
  .brand-dot {
    width: 22px; height: 22px;
    border-radius: 50%;
    background: var(--green);
    flex: none;
  }
  .brand-name {
    font-size: 19px;
    font-weight: 700;
    color: var(--blue-dark);
    line-height: 1.2;
  }
  .contact-list {
    list-style: none;
    border-left: 1px solid var(--rule);
    padding-left: 22px;
    font-size: 13px;
    color: var(--ink);
  }
  .contact-list li {
    display: flex;
    align-items: flex-start;
    gap: 10px;
    margin: 9px 0;
    line-height: 1.35;
  }
  .contact-list svg { flex: none; margin-top: 2px; }
  .accent-band { height: 28px; background: var(--green); }

  /* back */
  .back-top { height: 40px; background: var(--green); }
  .back-body {
    height: 226px;
    display: flex;
    align-items: center;
    justify-content: center;
  }
  .back-body .brand-mark { width: auto; }
  .back-body .brand-dot { width: 34px; height: 34px; }
  .back-body .brand-name { font-size: 30px; }
  .web-band {
    height: 54px;
    background: var(--blue);
    color: var(--white);
    font-size: 15px;
    font-weight: 600;
    letter-spacing: 2px;
    display: flex;
    align-items: center;
    justify-content: center;
  }
</style>
</head>
<body>
  <div class="side-label front">front</div>
  <section class="card front-card">
    <header class="name-band">
      <div class="person-name">Dale Whitcombe</div>
      <div class="person-title">Principal</div>
    </header>
    <div class="front-body">
      <div class="brand-mark">
        <span class="brand-dot"></span>
        <span class="brand-name">Korvale Power Solutions</span>
      </div>
      <ul class="contact-list">
        <li>
          <svg width="14" height="14" viewBox="0 0 24 24"><path fill="#3d84c6" d="M6.6 10.8a15 15 0 0 0 6.6 6.6l2.2-2.2c.3-.3.7-.4 1-.2 1.1.4 2.3.6 3.6.6.6 0 1 .4 1 1V20c0 .6-.4 1-1 1A17 17 0 0 1 3 4c0-.6.4-1 1-1h3.5c.6 0 1 .4 1 1 0 1.3.2 2.5.6 3.6.1.3 0 .7-.2 1z"/></svg>
          (555) 014-8820 ext. 42
        </li>
        <li>
          <svg width="14" height="14" viewBox="0 0 24 24"><rect x="2" y="5" width="20" height="14" rx="2" fill="#3d84c6"/><path d="M3 6l9 7 9-7" stroke="#fff" stroke-width="2" fill="none"/></svg>
          dale@korvalepower.com
        </li>
        <li>
          <svg width="14" height="14" viewBox="0 0 24 24"><circle cx="12" cy="12" r="10" fill="none" stroke="#3d84c6" stroke-width="2"/><path d="M2 12h20M12 2c3 3 3 17 0 20M12 2c-3 3-3 17 0 20" stroke="#3d84c6" stroke-width="1.6" fill="none"/></svg>
          www.korvalepower.com
        </li>
        <li>
          <svg width="14" height="14" viewBox="0 0 24 24"><path fill="#3d84c6" d="M12 2a7 7 0 0 0-7 7c0 5 7 13 7 13s7-8 7-13a7 7 0 0 0-7-7zm0 9.5A2.5 2.5 0 1 1 12 6.5a2.5 2.5 0 0 1 0 5z"/></svg>
          <span>480 Ridgeway Ave, Suite 210<br>Hartfield, OH 44170</span>
        </li>
      </ul>
    </div>
    <div class="accent-band"></div>
  </section>

  <div class="side-label back">back</div>
  <section class="card back-card">
    <div class="back-top"></div>
    <div class="back-body">
      <div class="brand-mark">
        <span class="brand-dot"></span>
        <span class="brand-name">Korvale Power Solutions</span>
      </div>
    </div>
    <footer class="web-band">www.korvalepower.com</footer>
  </section>
</body>
</html>
```